Zielgruppe
Wir sind ein Personaldienstleister und vermitteln ausländisches medizinisches Fachpersonal an deutsche Einrichtungen. Unsere Zielgruppe sind Krankenhäuser, Pflegeheime, Ärztehäuser, Praxen, Labore und weitere medizinische Institutionen.
Aufgabenstellung
Wir haben eine Infobroschüre sowie eine PowerPoint Präsentation bereits mit einem groben Design erstellt. Texte und Beispielbilder (Stockmaterial) sind ebenfalls vorhanden, gerne wünschen wir uns auch Eigeninitiative bei der Wahl der Bilder passend zum neuen Design.
Wir wünschen uns ein Redesign mit einem kreativen, einzigartigen Design. Zudem ist uns wichtig, dass unsere Infografiken qualitativ und hochwertig gestaltet werden.
Dieses Projekt ist mit zukünftigen Folgeprojekten verbunden, da wir weitere Präsentationen und Broschüren für andere Zielgruppen benötigen.

```html
<!DOCTYPE html>
<html lang="de">
<head>
<meta charset="utf-8">
<title>Veltaris HR – Fachkräfteeinwanderungsgesetz 2023</title>
<link rel="stylesheet" href="https://fonts.googleapis.com/css2?family=Roboto:wght@400;500;700&family=Roboto+Condensed:wght@700&display=swap">
<style>
  :root {
    --backdrop: #a9a9a9;
    --paper: #ffffff;
    --ink-black: #000000;
    --ink-white: #ffffff;
    --text-grey: #555a5c;
    --teal-dark: #1d4447;
    --teal-mid: #1f8a6e;
  }
  * { margin: 0; padding: 0; box-sizing: border-box; }
  html, body { width: 1200px; height: 870px; overflow: hidden; }
  body {
    background: var(--backdrop);
    font-family: "Roboto", Arial, sans-serif;
    position: relative;
  }
  .page {
    position: absolute;
    background: var(--paper);
    padding: 6px 5px;
  }
  .page--cover { left: 33px; top: 38px; width: 565px; height: 795px; }
  .page--facts { left: 606px; top: 38px; width: 566px; height: 795px; }
  .page__inner { position: relative; width: 100%; height: 100%; overflow: hidden; }

  /* Cover */
  .cover { background: var(--ink-black); color: var(--ink-white); }
  .brand {
    position: absolute; left: 22px; top: 22px;
    font-weight: 700; font-size: 28px; line-height: 34px;
    color: var(--ink-white);
  }
  .brand__rule {
    position: absolute; left: 22px; top: 62px; width: 251px; height: 2px;
    background: var(--ink-white);
  }
  .cover__title {
    position: absolute; left: 22px; top: 71px;
    font-weight: 500; font-size: 15px; line-height: 18px;
  }
  .cover__intro {
    position: absolute; left: 22px; top: 129px; width: 473px;
    font-size: 11.6px; line-height: 14.6px; text-align: justify;
    letter-spacing: 0.1px;
  }
  .cover__photo {
    position: absolute; left: 0; top: 232px; width: 100%; height: 552px;
    background:
      radial-gradient(ellipse 45% 35% at 50% 40%, #7a4218 0%, rgba(80,40,15,0.6) 45%, rgba(0,0,0,0) 75%),
      linear-gradient(180deg, #000 0%, #0a0604 55%, #cfcfd2 75%, #e2e2e4 88%, #8b0d12 100%);
  }

  /* Facts */
  .facts__header {
    position: absolute; left: 0; top: 0; width: 100%; height: 219px;
    background: linear-gradient(180deg, #000 0%, #000 77%, #d8d8d8 78%, #9a9a9a 84%, #b8b8b8 100%);
  }
  .facts__mark {
    position: absolute; left: 286px; top: 42px; width: 44px; height: 44px;
    border-radius: 50%; background: var(--teal-mid); border: 3px solid var(--paper);
  }
  .facts__brand {
    position: absolute; left: 338px; top: 55px;
    font-size: 14px; line-height: 18px; font-weight: 500; color: var(--ink-white);
    white-space: nowrap;
  }
  .facts__title {
    position: absolute; left: 193px; top: 100px;
    font-family: "Roboto Condensed", "Arial Narrow", sans-serif;
    font-weight: 700; font-size: 31px; line-height: 36px; color: var(--ink-white);
    white-space: nowrap;
  }
  .fact {
    position: absolute; white-space: nowrap;
    font-size: 11.3px; line-height: 13.4px; color: var(--text-grey);
  }
  .fact::before {
    content: ""; position: absolute; left: -26px; top: -3px;
    width: 20px; height: 20px; border-radius: 50%;
    border: 1.5px solid var(--teal-dark); background: var(--paper);
  }
  .fact::after {
    content: ""; position: absolute; left: -21px; top: 2px;
    width: 10px; height: 10px; border-radius: 50%;
    background: var(--teal-dark);
  }
  .fact-col--left .fact { left: 50px; }
  .fact-col--right .fact { left: 313px; }
  .timeline {
    position: absolute; width: 0; border-left: 1px dashed var(--teal-dark);
  }
  .facts__footer {
    position: absolute; left: 0; bottom: 0; width: 100%; height: 25px;
    background: var(--teal-dark); color: var(--ink-white);
    font-size: 7.5px;
  }
  .facts__footer span {
    position: absolute; top: 50%; transform: translate(-50%, -50%); white-space: nowrap;
  }
</style>
</head>
<body>
  <section class="page page--cover">
    <div class="page__inner cover">
      <div class="brand">Veltaris HR</div>
      <div class="brand__rule"></div>
      <h1 class="cover__title">Deutschlands neues<br>Fachkräfteeinwanderungsgesetz<br>für 2023</h1>
      <p class="cover__intro">Am 30. November 2022 hat die deutsche Bundesregierung die Eckpunkte des neuen Fachkräfteeinwanderungsgesetztes verabschiedet. Damit will Deutschland massiv die Bildungschancen verbessern, Aus- und Weiterbildung gezielt voranbringen sowie die Einwanderung für Fachkräfte erheblich erleichtern – insbesondere für Personen aus Drittstaaten und somit auch für erwerbstätige Menschen aus der Türkei.<br>Wir haben die wichtigsten Fakten für Sie übersichtlich im Folgenden zusammengefasst.</p>
      <div class="cover__photo" role="img" aria-label="Foto: Richterhammer aus Holz auf einem aufgeschlagenen Gesetzbuch vor schwarzem Hintergrund"></div>
    </div>
  </section>

  <section class="page page--facts">
    <div class="page__inner">
      <div class="facts__header" role="img" aria-label="Illustration: großes weißes Paragraphenzeichen auf grauem Holzboden vor schwarzem Hintergrund"></div>
      <div class="facts__mark"></div>
      <div class="facts__brand">Veltaris HR</div>
      <h2 class="facts__title">Die Fakten im Überblick</h2>

      <div class="timeline" style="left:34px;top:263px;height:339px;"></div>
      <div class="timeline" style="left:297px;top:263px;height:379px;"></div>

      <div class="fact-col--left">
        <p class="fact" style="top:247px;">Menschen aus Drittstaaten mit einem<br>deutschen oder einem in Deutschland<br>anerkannten Abschluss sollen fortan jede<br>qualifizierte Beschäftigung ausüben<br>können. Ein Beispiel: eine als Kauffrau für<br>Büromanagement anerkannte Fachkraft<br>kann auch im Bereich Logistik als Fachkraft<br>beschäftigt werden.</p>
        <p class="fact" style="top:367px;">Stärkung der Bildungsmigration, indem die<br>Aufnahme einer Berufsausbildung oder<br>eines Studiums erleichtert wird</p>
        <p class="fact" style="top:421px;">Für die „Blaue Karte EU“ wird die<br>Gehaltsschwelle abgesenkt und somit<br>attraktiver für Berufsanfänger:innen</p>
        <p class="fact" style="top:475px;">In Zukunft soll ein ausländischer Berufs-<br>oder Hochschulabschluss (mind. 2 Jahre)<br>und eine mindestens zweijährige Berufser-<br>fahrung in dem angestrebten (nicht-regle-<br>mentierten) Beruf für einen Aufenthalt zur<br>Erwerbstätigkeit ausreichen die formale<br>Anerkennung des ausländischen<br>Berufsabschlusses ist nicht erforderlich</p>
        <p class="fact" style="top:595px;">Für Fachkräfte aus Drittstaaten besteht die<br>Möglichkeit erst nach der Einreise die<br>Anerkennung ihres ausländischen Berufsab-<br>schlusses anerkennen zu lassen und neben-<br>her bereits eine qualifizierte Beschäftigung<br>auszuüben</p>
      </div>

      <div class="fact-col--right">
        <p class="fact" style="top:247px;">Die Chancenkarte ist neu und richtet sich an<br>qualifizierte Drittstaatsangehörige, die noch<br>keinen Arbeitsvertrag haben. Sie garantiert<br>einen Aufenthaltstitel für bis zu einem Jahr<br>für die Arbeitssuche in Deutschland und<br>berechtigt bereits zu Probe- bzw. Neben-<br>beschäftigungen</p>
        <p class="fact" style="top:354px;">Basieren soll die sogenannte Chancenkarte<br>auf Basis eines Punktesystems, ähnlich<br>dem von Kanada. Zu den Auswahlkriterien<br>gehören die QUALIFIKATION, SPRACH-<br>KENNTNISSE, BERUFSERFAHRUNG,<br>DEUTSCHLANDBEZUG und das ALTER.</p>
        <p class="fact" style="top:448px;">Zudem ist die kurzzeitig befristete Bes-<br>chäftigungen im Rahmen von Kontin-<br>genten geplant, ohne spezielle Qualifika-<br>tionsanforderungen</p>
        <p class="fact" style="top:515px;">Die Sprachförderung im In- und Ausland<br>soll deutlich ausgebaut werden</p>
        <p class="fact" style="top:555px;">Das Anerkennungsverfahren, das<br>Beschleunigte Fachkräfteverfahren<br>sowie das Visumverfahren sollen opti-<br>miert und die Bearbeitungszeiten strikter<br>eingehalten werden</p>
        <p class="fact" style="top:635px;">Erleichterung der Einbürgerung: Die<br>Mindestaufenthaltsdauer soll von 8 auf<br>5 Jahre herabgesetzt werden, bei<br>besonderen Integrationsleistungen<br>sogar auf 3 Jahre – außerdem muss die<br>alte Staatsbürgerschaft nicht mehr<br>aufgegeben werden</p>
      </div>

      <footer class="facts__footer">
        <span style="left:104px;">+49 211 470 38 215</span>
        <span style="left:282px;">hr@veltaris.com</span>
        <span style="left:447px;">www.veltaris-hr.com</span>
      </footer>
    </div>
  </section>
</body>
</html>
```